DJ business brochure

I need a business brochure for my DJ business. Something that represents my business being owned and operated by first responders yet elegant enough to attract customers for weddings.

I do not have a preference on a type of brochure. Tri-fold or standard. The front page should have our logo and the name of our company. Under the name of our company it should say "Owned and operated by First Responders"

Bullet points for the brochure
LED up lighting.
Video projection
Dancing in the clouds
Top rated and experienced DJ's
Fun, crowd interactive DJ's
Text song request line.
Professional reception planning.

It should say somewhere on the brochure "When you choose Harbor 9 you become part of the first responder family."

Contact information Lou@harbor9dj.net Phone or text (507) 318-2674

Please use some fun pictures of weddings or people dancing. Does not specifically need to be from our sites.

Target Market(s)

Brides/Groom

Industry/Entity Type

Wedding/Party DJ

Requirements
Must have
• I want the wow factor. Something that when people look at the brochure they are drawn to read it. Email Lou@Harbor9DJ.net Phone (507) 318-2674
Nice to have
• Nice to have a flaming vinyl record or a flaming musical note somewhere in the brochure.

```html
<!DOCTYPE html>
<html lang="en">
<head>
<meta charset="utf-8">
<title>Harbor 9 DJ Tri-fold Brochure</title>
<link rel="stylesheet" href="https://fonts.googleapis.com/css2?family=Open+Sans:wght@400;600;700;800&display=swap">
<style>
:root{
  --backdrop:#7a7a7a;
  --ink:#0d0d0f;
  --panel-dark:#141416;
  --panel-dark-2:#1f1f22;
  --red:#c8161d;
  --red-deep:#8e0c11;
  --red-bright:#e0262b;
  --silver:#bdbdbd;
  --white:#ffffff;
  --muted:#c9c9c9;
  --photo-purple:#7c3fb0;
  --photo-magenta:#c04bd0;
  --photo-blue:#2a55c8;
}
*{box-sizing:border-box;margin:0;padding:0}
html,body{width:1200px;height:2400px;overflow:hidden}
body{background:var(--backdrop);font-family:"Open Sans",Arial,sans-serif;color:var(--white);position:relative}

.spread{position:absolute;left:40px;width:1120px;height:860px;display:grid;grid-template-columns:repeat(3,1fr);box-shadow:0 14px 40px rgba(0,0,0,.35)}
.spread--outside{top:230px}
.spread--inside{top:1310px}

.panel{position:relative;overflow:hidden;background:linear-gradient(180deg,var(--panel-dark-2),var(--panel-dark) 60%,#0a0a0b)}
.panel--red{background:radial-gradient(ellipse at 50% 40%,var(--red-bright),var(--red) 45%,var(--red-deep))}

.photo{position:absolute;background:linear-gradient(135deg,var(--photo-blue),var(--photo-purple) 50%,var(--photo-magenta))}
.photo--warm{background:linear-gradient(135deg,#3a1760,#a63fb8 55%,#f0b8e8)}
.photo--club{background:linear-gradient(160deg,#1b1f4a,#4a3aa0 50%,#b06ad8)}
.photo--gear{background:linear-gradient(180deg,#1a2035,#2c3d78 50%,#0d0f18)}
.photo-round{border-radius:50%;border:4px solid var(--white)}

.swoosh{position:absolute;left:0;width:100%}

.footer-bar{position:absolute;left:0;right:0;bottom:0;height:44px;background:#0a0a0b;border-top:3px solid var(--red);display:flex;align-items:center;justify-content:center;font-weight:700;font-size:15px;letter-spacing:1px;color:var(--white)}

.brand{position:absolute;left:50%;transform:translateX(-50%);display:flex;align-items:center;gap:10px;font-weight:800;font-size:30px;color:var(--white);white-space:nowrap}
.brand-dot{width:34px;height:34px;border-radius:50%;background:var(--red)}

.heading{font-weight:700;font-size:20px;letter-spacing:1px;text-transform:uppercase}
.body-copy{font-size:11.5px;line-height:1.6;color:var(--muted)}

.pill{display:inline-block;border-radius:20px;font-weight:700;text-transform:uppercase;font-size:12px;padding:7px 18px;letter-spacing:.5px}
.pill--red{background:var(--red);color:var(--white)}
.pill--dark{background:#0d0d0f;color:var(--white);border:2px solid var(--white)}
.pill--outline{border:2px solid var(--red);color:var(--white);font-size:16px}

/* outside left */
.about{position:absolute;left:34px;right:30px;top:330px}
.about .heading{margin-bottom:12px}
.service-list{list-style:none;margin:14px 0 18px;font-size:12px;line-height:1.8;color:var(--white)}
.service-list li::before{content:"";display:inline-block;width:6px;height:6px;background:var(--red);border-radius:50%;margin-right:8px;vertical-align:middle}

/* outside middle */
.intro{position:absolute;left:36px;right:36px;top:420px;text-align:center;font-size:15px;line-height:1.5;font-style:normal}
.intro p+p{margin-top:14px}
.book{position:absolute;left:0;right:0;top:580px;text-align:center}
.socials{display:flex;justify-content:center;gap:10px;margin-top:12px}
.socials span{width:24px;height:24px;border-radius:50%;border:2px solid var(--white)}
.contact{position:absolute;left:0;right:0;top:670px;text-align:center;font-size:14px;line-height:1.5}
.contact strong{display:block;font-size:16px}
.phone-line{position:absolute;left:0;right:0;bottom:14px;text-align:center;font-weight:700;font-size:17px;letter-spacing:1px}

/* cover */
.tagline{position:absolute;left:0;right:0;top:705px;text-align:center;font-weight:700;font-size:25px;line-height:1.2;text-transform:uppercase}

/* inside middle */
.services-title{position:absolute;left:0;right:0;top:40px;text-align:center}
.services-grid{position:absolute;left:26px;right:26px;top:100px;display:grid;grid-template-columns:repeat(3,1fr);row-gap:26px;text-align:center}
.service-icon{width:64px;height:64px;margin:0 auto 8px;border-radius:50%;background:var(--white);display:flex;align-items:center;justify-content:center}
.service-icon svg{width:34px;height:34px}
.service-label{font-size:10.5px;font-weight:700;text-transform:uppercase;line-height:1.3}
.family{position:absolute;left:30px;right:30px;top:590px;text-align:center}
.family .site{font-weight:700;font-size:19px;letter-spacing:1px}
.family p{font-size:15px;line-height:1.45;margin-top:10px}

/* inside right */
.events{position:absolute;left:34px;right:30px;top:300px}
.events .heading{font-size:19px;margin-bottom:14px}
.events p+p{margin-top:10px}
</style>
</head>
<body>

<!-- OUTSIDE SPREAD -->
<section class="spread spread--outside" aria-label="Brochure outside">
  <!-- inside flap -->
  <article class="panel">
    <div class="photo photo--club" style="left:0;top:0;width:100%;height:230px" role="img" aria-label="DJ performing at the decks under blue club lights"></div>
    <svg class="swoosh" style="top:200px" height="60" viewBox="0 0 373 60" preserveAspectRatio="none"><path d="M0 60 L0 40 Q190 0 373 20 L373 60Z" fill="#1f1f22"/><path d="M0 40 Q190 0 373 20" stroke="#c8161d" stroke-width="4" fill="none"/></svg>
    <div class="photo photo--warm photo-round" style="left:40px;top:220px;width:90px;height:90px" role="img" aria-label="Guests dancing at a reception"></div>
    <div class="photo photo--club photo-round" style="left:140px;top:235px;width:80px;height:80px" role="img" aria-label="Dance floor with purple lighting"></div>
    <div class="about">
      <h2 class="heading">DJ Harbor</h2>
      <p class="body-copy">Whether you are planning a wedding, a reception or a milestone party, our crew brings the sound, the lights and the energy. Every event is handled with the same care and calm focus we bring to our day jobs.</p>
      <ul class="service-list">
        <li>LED up lighting</li>
        <li>Video projection</li>
        <li>Dancing in the clouds</li>
        <li>Text song request line</li>
        <li>Professional reception planning</li>
      </ul>
      <span class="pill pill--red">Book your event today</span>
    </div>
    <div class="footer-bar">www.Harbor9DJ.net</div>
  </article>

  <!-- back panel -->
  <article class="panel panel--red">
    <div class="photo photo--warm" style="left:0;top:0;width:100%;height:250px" role="img" aria-label="Decorated wedding reception hall in purple light"></div>
    <svg class="swoosh" style="top:220px" height="50" viewBox="0 0 373 50" preserveAspectRatio="none"><path d="M0 50 L0 30 Q190 -10 373 30 L373 50Z" fill="#c8161d"/><path d="M0 30 Q190 -10 373 30" stroke="#0d0d0f" stroke-width="5" fill="none"/></svg>
    <div class="brand" style="top:310px"><span class="brand-dot"></span>Harbor 9</div>
    <div class="intro">
      <p>Professional DJ / VJ services operated by first responders. Top rated for weddings. Exclusive discounts for public safety professionals.</p>
      <p>Call, text or email us for information and quotes.</p>
    </div>
    <div class="book">
      <span class="pill pill--dark">Book your event today!</span>
      <div class="socials"><span></span><span></span></div>
    </div>
    <div class="contact">
      <strong>DJ HARBOR</strong>
      (507) 318-2674<br>Lou@harbor9dj.net<br>www.Harbor9DJ.net
    </div>
    <div class="footer-bar" style="background:#0a0a0b">
      <svg width="16" height="16" viewBox="0 0 24 24" style="margin-right:8px"><path d="M6.6 10.8a15 15 0 006.6 6.6l2.2-2.2a1 1 0 011-.25 11 11 0 003.6.6 1 1 0 011 1V20a1 1 0 01-1 1A17 17 0 013 4a1 1 0 011-1h3.5a1 1 0 011 1 11 11 0 00.6 3.6 1 1 0 01-.25 1z" fill="#fff"/></svg>
      (507) 318-2674
    </div>
  </article>

  <!-- front cover -->
  <article class="panel">
    <svg class="swoosh" style="top:0" height="120" viewBox="0 0 373 120" preserveAspectRatio="none"><path d="M0 0 H373 V40 Q190 0 0 100Z" fill="#4a4a4e"/><path d="M0 100 Q190 0 373 40" stroke="#bdbdbd" stroke-width="3" fill="none"/></svg>
    <div class="photo photo--warm" style="left:30px;top:60px;width:313px;height:500px;border-radius:70px 0 0 0" role="img" aria-label="Bride and groom sharing their first dance under falling confetti"></div>
    <svg class="swoosh" style="top:530px" height="60" viewBox="0 0 373 60" preserveAspectRatio="none"><path d="M0 60 L0 20 Q190 60 373 0 L373 60Z" fill="#1a1a1c"/><path d="M0 20 Q190 60 373 0" stroke="#c8161d" stroke-width="5" fill="none"/></svg>
    <div class="brand" style="top:620px"><span class="brand-dot"></span>Harbor 9</div>
    <h1 class="tagline">Owned and operated<br>by first responders</h1>
    <div class="footer-bar">www.Harbor9DJ.net</div>
  </article>
</section>

<!-- INSIDE SPREAD -->
<section class="spread spread--inside" aria-label="Brochure inside">
  <article class="panel">
    <div class="photo photo--warm" style="left:0;top:0;width:100%;height:250px" role="img" aria-label="Bride and groom dancing in purple light"></div>
    <svg class="swoosh" style="top:220px" height="50" viewBox="0 0 373 50" preserveAspectRatio="none"><path d="M0 50 L0 30 Q190 0 373 30 L373 50Z" fill="#1f1f22"/></svg>
    <div class="events" style="top:290px">
      <h2 class="heading">DJ Harbor</h2>
      <p class="body-copy">Choose the setup that fits your day, from a single speaker for the ceremony to a full dance floor rig with lighting and video. We listen first, plan every cue with you, and keep the room moving from the first dance to the last song of the night.</p>
    </div>
    <div class="photo photo--gear" style="left:0;bottom:0;width:100%;height:330px" role="img" aria-label="DJ controller and mixer lit in blue"></div>
    <svg class="swoosh" style="bottom:20px" height="40" viewBox="0 0 373 40" preserveAspectRatio="none"><path d="M0 40 L0 20 Q190 40 373 10 L373 40Z" fill="#0a0a0b"/><path d="M0 20 Q190 40 373 10" stroke="#c8161d" stroke-width="4" fill="none"/></svg>
  </article>

  <article class="panel panel--red">
    <h2 class="heading services-title">Our Services</h2>
    <div class="services-grid">
      <div><div class="service-icon"><svg viewBox="0 0 24 24"><path d="M12 2a7 7 0 00-4 12.7V18h8v-3.3A7 7 0 0012 2zM9 20h6v2H9z" fill="#c8161d"/></svg></div><div class="service-label">LED up<br>lighting</div></div>
      <div><div class="service-icon"><svg viewBox="0 0 24 24"><rect x="2" y="7" width="20" height="11" rx="2" fill="#c8161d"/><circle cx="15" cy="12.5" r="3" fill="#fff"/></svg></div><div class="service-label">Video<br>projection</div></div>
      <div><div class="service-icon"><svg viewBox="0 0 24 24"><path d="M6 19a4 4 0 010-8 6 6 0 0111.5-1.5A4.5 4.5 0 0118 19z" fill="#c8161d"/></svg></div><div class="service-label">Dancing in<br>the clouds</div></div>
      <div><div class="service-icon"><svg viewBox="0 0 24 24"><circle cx="9" cy="14" r="5" stroke="#c8161d" stroke-width="2.5" fill="none"/><circle cx="15" cy="14" r="5" stroke="#c8161d" stroke-width="2.5" fill="none"/></svg></div><div class="service-label">Weddings</div></div>
      <div><div class="service-icon"><svg viewBox="0 0 24 24"><path d="M3 10h4l9-5v14l-9-5H3z" fill="#c8161d"/><path d="M18 9a4 4 0 010 6" stroke="#c8161d" stroke-width="2" fill="none"/></svg></div><div class="service-label">Fun, crowd<br>interactive</div></div>
      <div><div class="service-icon"><svg viewBox="0 0 24 24"><rect x="4" y="12" width="16" height="9" fill="#c8161d"/><rect x="11" y="6" width="2" height="6" fill="#c8161d"/><circle cx="12" cy="4.5" r="1.5" fill="#c8161d"/></svg></div><div class="service-label">Birthday<br>parties</div></div>
      <div><div class="service-icon"><svg viewBox="0 0 24 24"><path d="M12 2l3 6.5 7 .8-5.2 4.8 1.5 7L12 17.6 5.7 21l1.5-7L2 9.3l7-.8z" fill="#c8161d"/></svg></div><div class="service-label">Top rated and<br>experienced DJ's</div></div>
      <div><div class="service-icon"><svg viewBox="0 0 24 24"><path d="M3 4h18v12H8l-5 4z" fill="#c8161d"/></svg></div><div class="service-label">Text song<br>request line</div></div>
      <div><div class="service-icon"><svg viewBox="0 0 24 24"><rect x="5" y="3" width="14" height="18" rx="2" fill="#c8161d"/><path d="M8 9h8M8 13h8M8 17h5" stroke="#fff" stroke-width="1.8"/></svg></div><div class="service-label">Professional<br>reception planning</div></div>
    </div>
    <div class="family">
      <div class="site">www.Harbor9DJ.net</div>
      <p>When you choose Harbor 9 you become part of the first responder family.</p>
    </div>
    <div class="photo photo--club photo-round" style="left:110px;top:720px;width:90px;height:90px" role="img" aria-label="Crowd dancing at a party"></div>
  </article>

  <article class="panel">
    <div class="photo photo--club" style="left:0;top:0;width:100%;height:260px" role="img" aria-label="Concert crowd with hands raised under stage lights"></div>
    <svg class="swoosh" style="top:230px" height="50" viewBox="0 0 373 50" preserveAspectRatio="none"><path d="M0 50 L0 30 Q190 0 373 30 L373 50Z" fill="#1f1f22"/></svg>
    <div class="events">
      <h2 class="heading">Available for all music events!</h2>
      <p class="body-copy">From weddings and proms to company parties and fundraisers, we bring a full show to any venue, large or small.</p>
      <p class="body-copy">Our team has served the community for years. We know how to read a room, keep a schedule and make every guest feel welcome.</p>
      <p class="body-copy">Text in your requests during the party and watch the floor fill up.</p>
    </div>
    <svg class="swoosh" style="top:560px" height="60" viewBox="0 0 373 60" preserveAspectRatio="none"><path d="M0 60 Q190 -10 373 20" stroke="#c8161d" stroke-width="5" fill="none"/></svg>
    <div class="photo photo--warm photo-round" style="left:40px;top:610px;width:110px;height:110px" role="img" aria-label="Couple dancing at their reception"></div>
    <div class="brand" style="top:630px;left:255px;font-size:26px"><span class="brand-dot" style="width:28px;height:28px"></span>Harbor 9</div>
    <div style="position:absolute;left:0;right:0;top:770px;text-align:center"><span class="pill pill--outline">(507) 318-2674</span></div>
  </article>
</section>

</body>
</html>
```